M Website

We need a website design for a construction plant company. You may use a combination of our photos and the stock images. See the logo for company colours. It also be of great value to see moving pictures like the ones on the link: https://www.bellwickventures.co.za/copy-of-about-us. See our uploaded files for content.

Target Market(s)

Construction

Number of Pages Required

5+ page

```html
<!DOCTYPE html>
<html lang="en">
<head>
<meta charset="utf-8">
<title>K4 Haulage &amp; Plant Hire</title>
<link href="https://fonts.googleapis.com/css2?family=Montserrat:wght@500;600;700;800&family=Questrial&family=Open+Sans:ital,wght@1,400;1,600&display=swap" rel="stylesheet">
<style>
:root{
  --yellow:#fcc200;
  --yellow-deep:#f5b400;
  --black:#111111;
  --ink:#222222;
  --text:#555555;
  --muted:#888888;
  --line:#e4e4e4;
  --pale:#f2f4f7;
  --white:#ffffff;
}
*{box-sizing:border-box;margin:0;padding:0}
html,body{width:1200px;height:2786px;overflow:hidden;background:var(--white)}
body{position:relative;font-family:"Questrial",sans-serif;color:var(--text)}
.abs{position:absolute}
.center{text-align:center}

/* header */
.topbar{left:0;top:0;width:1200px;height:54px;background:var(--black)}
.topbar .contact{position:absolute;top:15px;font-size:13px;color:#ddd;display:flex;align-items:center;gap:8px;letter-spacing:.5px}
.topbar .contact .ring{width:24px;height:24px;border:2px solid var(--yellow);border-radius:50%;display:flex;align-items:center;justify-content:center}
.topbar .contact b{color:var(--yellow);font-weight:400}
.navbar{left:0;top:54px;width:1200px;height:46px;background:var(--yellow)}
.nav{position:absolute;left:450px;top:0;display:flex;gap:60px;height:46px;align-items:center}
.nav a{font-family:"Montserrat",sans-serif;font-weight:700;font-size:12px;color:var(--ink);text-decoration:none;letter-spacing:.3px;position:relative}
.nav a.active::after{content:"";position:absolute;left:0;right:0;bottom:-6px;height:2px;background:var(--ink)}
.brand-plate{left:150px;top:0;width:196px;height:118px;background:var(--black);clip-path:polygon(0 0,100% 0,100% 72%,88% 100%,12% 100%,0 72%);display:flex;align-items:center;justify-content:center;flex-direction:column}
.brand-name{font-family:"Montserrat",sans-serif;font-weight:800;font-size:44px;color:var(--yellow);line-height:1}
.brand-sub{font-family:"Montserrat",sans-serif;font-weight:800;font-size:9px;color:var(--yellow);letter-spacing:1px;margin-top:4px}

/* hero */
.hero{left:0;top:100px;width:1200px;height:478px;background:linear-gradient(90deg,#f3f0ea 0%,#e9e2d2 30%,#d9cdb0 55%,#ece6d8 80%,#f6f3ee 100%)}
.hero-rule{left:0;top:578px;width:1200px;height:4px;background:var(--yellow)}
.hero-title{left:168px;top:252px;font-family:"Montserrat",sans-serif;font-weight:700;font-size:25px;line-height:36px;color:var(--ink)}
.hero-title span{color:var(--yellow-deep)}
.btn{display:inline-block;background:var(--yellow);color:var(--white);font-family:"Montserrat",sans-serif;font-weight:700;font-size:11px;text-align:center}
.hero-btn{left:166px;top:328px;width:110px;height:32px;line-height:32px}
.hero-dots{left:576px;top:556px;width:100px;height:22px;background:var(--yellow);clip-path:polygon(10% 0,90% 0,100% 100%,0 100%);display:flex;align-items:center;justify-content:center;gap:7px;padding-top:4px}
.hero-dots i{width:7px;height:7px;border-radius:50%;background:var(--white);display:block}
.hero-dots i.on{width:10px;height:10px;border:2px solid var(--white);background:transparent}

/* section titles */
.sec-title{left:0;width:1200px;font-family:"Montserrat",sans-serif;font-weight:700;font-size:26px;color:var(--yellow-deep);text-align:center}
.sec-title span{color:var(--ink)}
.sec-sub{left:0;width:1200px;font-family:"Montserrat",sans-serif;font-weight:700;font-size:13px;color:var(--ink);text-align:center;letter-spacing:.5px}
.sec-text{font-size:12.5px;line-height:23px;color:var(--text);text-align:center}

/* about */
.video{left:386px;top:822px;width:492px;height:332px;box-shadow:0 8px 28px rgba(0,0,0,.18);background:var(--white)}
.video-frame{position:absolute;left:0;top:0;width:492px;height:298px;background:linear-gradient(160deg,#8a7a5c 0%,#5d5344 40%,#3e4f7a 70%,#5d5a4c 100%)}
.video-bar{position:absolute;left:0;top:298px;width:492px;height:34px;background:#1c1c1c}
.play{position:absolute;left:222px;top:124px;width:48px;height:48px;border-radius:50%;background:rgba(0,0,0,.55);border:2px solid var(--white)}
.pillar{width:220px;text-align:center}
.pillar h3{font-family:"Montserrat",sans-serif;font-weight:700;font-size:16px;color:var(--yellow-deep);margin:14px 0 12px}
.pillar p{font-family:"Open Sans",sans-serif;font-style:italic;font-size:13px;line-height:26px;color:#444}

/* offerings */
.band-edge{top:1226px;width:30px;height:126px;background:var(--pale)}
.title-rule{left:556px;width:88px;height:2px;background:#bbb}
.offer-card{top:1355px;width:206px;height:158px;background:var(--white);border:1px solid #ececec;box-shadow:0 4px 14px rgba(0,0,0,.06);text-align:center;padding-top:30px}
.offer-card.active{border:2px solid var(--yellow);box-shadow:0 8px 24px rgba(0,0,0,.14)}
.offer-card p{font-size:13px;line-height:20px;color:var(--text);margin-top:16px}
.offer-card.active p{font-family:"Montserrat",sans-serif;font-weight:700;color:var(--ink);font-size:12.5px}
.shelf{left:160px;width:884px}

/* why choose */
.trait{width:260px}
.trait h4{font-family:"Montserrat",sans-serif;font-weight:700;font-size:13px;color:var(--ink);letter-spacing:.8px;margin-bottom:4px}
.trait p{font-size:12px;line-height:18px;color:var(--text)}
.trait.left{text-align:right}
.hub-name{font-family:"Montserrat",sans-serif;font-weight:800;font-size:46px;color:var(--yellow-deep);line-height:1}

/* call to action */
.cta{left:0;top:2178px;width:1200px;height:293px;background:linear-gradient(90deg,#23252a 0%,#3a3a34 45%,#2c2d2c 70%,#4a4430 100%)}
.cta-title{left:0;top:2248px;width:1200px;text-align:center;font-family:"Montserrat",sans-serif;font-weight:700;font-size:25px;color:var(--yellow);letter-spacing:.5px}
.cta-sub{left:0;top:2295px;width:1200px;text-align:center;font-size:15px;color:var(--white)}
.cta-btn{left:496px;top:2346px;width:206px;height:46px;line-height:46px;font-size:13px;color:var(--ink)}

/* footer */
.footer{left:0;top:2471px;width:1200px;height:271px;background:var(--yellow)}
.foot-h{font-family:"Montserrat",sans-serif;font-weight:700;font-size:12.5px;color:var(--ink);letter-spacing:.5px}
.links{list-style:none}
.links li{font-size:12.5px;color:var(--ink);line-height:27px;padding-left:16px;position:relative}
.links li::before{content:"»";position:absolute;left:0;color:#7a5d00}
.crow{display:flex;gap:12px;align-items:flex-start;font-size:11.5px;line-height:17px;color:var(--ink);margin-bottom:12px}
.pin{flex:0 0 26px;width:26px;height:26px;border-radius:50%;background:#6b5200;display:flex;align-items:center;justify-content:center}
.field{width:176px;height:27px;background:var(--white);border:1px solid #e1b000;font-size:10px;color:#777;padding:6px 6px;margin-bottom:6px}
.field.msg{height:52px}
.submit{width:98px;height:30px;line-height:30px;background:var(--black);color:var(--white);font-family:"Montserrat",sans-serif;font-weight:700;font-size:12px;text-align:center}
.socials{display:flex;gap:8px}
.socials i{display:block;width:24px;height:24px;background:#1b4f8a}
.foot-brand{font-family:"Montserrat",sans-serif;font-weight:800;font-size:40px;color:#6b5200;line-height:1}
.copy{left:0;top:2742px;width:1200px;height:44px;background:var(--black);color:#ddd;font-size:12.5px;text-align:center;line-height:44px}
</style>
</head>
<body>

<!-- header -->
<div class="abs topbar">
  <div class="contact" style="left:608px">
    <span class="ring"><svg width="12" height="12" viewBox="0 0 24 24"><path d="M6 2l4 4-2 3c1 3 4 6 7 7l3-2 4 4-3 4C10 22 2 14 2 5z" fill="#fcc200"/></svg></span>
    <span>CALL : <b>123-456-7890</b></span>
  </div>
  <div class="contact" style="left:800px">
    <span class="ring"><svg width="12" height="10" viewBox="0 0 24 18"><rect x="1" y="1" width="22" height="16" fill="none" stroke="#fcc200" stroke-width="2.5"/><path d="M1 1l11 9 11-9" fill="none" stroke="#fcc200" stroke-width="2.5"/></svg></span>
    <span>EMAIL : <b>info@k4haulage.co.za</b></span>
  </div>
</div>
<div class="abs navbar">
  <nav class="nav">
    <a class="active">HOME</a><a>ABOUT US</a><a>OFFERINGS</a><a>WORK GALLERY</a><a>CONTACT US</a>
  </nav>
</div>
<div class="abs brand-plate">
  <div class="brand-name">K4</div>
  <div class="brand-sub">HAULAGE &amp; PLANT HIRE</div>
</div>

<!-- hero -->
<div class="abs hero" role="img" aria-label="Photo of a smiling site worker in a hard hat and safety vest in front of colleagues reviewing plans"></div>
<div class="abs hero-rule"></div>
<h1 class="abs hero-title">WE WILL MAKE YOU PROUD.HIRE US AND<br><span>START YOUR DREAM PROJECT NOW.</span></h1>
<a class="abs btn hero-btn">GET STARTED</a>
<div class="abs hero-dots"><i></i><i></i><i class="on"></i><i></i><i></i></div>

<!-- about -->
<h2 class="abs sec-title" style="top:644px">ABOUT K4</h2>
<div class="abs sec-sub" style="top:678px">LOGISTICS &amp; PLANT HIRE</div>
<p class="abs sec-text" style="left:160px;top:706px;width:880px">K4 Haulage and Plant Hire (Pty) Ltd is a family owned Construction and Plant Hire company operating mainly from the K4 head office in Thornbury (Ashvale). K4 Haulage and Plant Hire (Pty) Ltd was established in 2011, and has worked in various municipal jurisdictions across the region. Since inception, K4 Haulage and Plant Hire (Pty) Ltd has worked on a number of projects, acquiring a track record primarily in the following disciplines, amongst the company’s offerings and/or services.</p>

<div class="abs pillar" style="left:144px;top:896px">
  <svg width="56" height="56" viewBox="0 0 56 56"><circle cx="28" cy="28" r="24" fill="none" stroke="#f5b400" stroke-width="3"/><circle cx="28" cy="28" r="15" fill="none" stroke="#f5b400" stroke-width="3"/><circle cx="28" cy="28" r="6" fill="#f5b400"/><path d="M28 28L48 8M42 8h6v6" fill="none" stroke="#f5b400" stroke-width="3"/></svg>
  <h3>OUR GOAL</h3>
  <p>The Goal for Top-Flight builders<br>is to be a nationwide builder.<br>Covering ever size of projects.</p>
</div>
<div class="abs pillar" style="left:894px;top:896px">
  <svg width="56" height="56" viewBox="0 0 56 56"><path d="M6 48L28 12l22 36z" fill="none" stroke="#f5b400" stroke-width="3"/><path d="M28 12V2l10 4-10 4" fill="#f5b400" stroke="#f5b400" stroke-width="2"/><path d="M17 30l6 4 5-5 5 5 6-4" fill="none" stroke="#f5b400" stroke-width="3"/></svg>
  <h3>OUR MISSION</h3>
  <p>Quality, comfort, &amp; attention you<br>deserve. Provide in<br>every Porject we works.</p>
</div>

<div class="abs video">
  <div class="video-frame" role="img" aria-label="Video still of road workers in hard hats and vests digging at a trench"></div>
  <div class="play"><svg width="44" height="44" viewBox="0 0 44 44"><path d="M17 12l15 10-15 10z" fill="#fff"/></svg></div>
  <div class="video-bar">
    <svg width="492" height="34" viewBox="0 0 492 34">
      <rect x="0" y="0" width="492" height="4" fill="#555"/><rect x="0" y="0" width="80" height="4" fill="#e52d27"/>
      <rect x="14" y="13" width="4" height="12" fill="#fff"/><rect x="21" y="13" width="4" height="12" fill="#fff"/>
      <path d="M40 13l8 6-8 6zM48 13h3v12h-3z" fill="#fff"/>
      <path d="M66 16h4l5-4v14l-5-4h-4z" fill="#fff"/>
      <text x="104" y="23" fill="#ddd" font-size="10" font-family="sans-serif">0:35 / 2:25</text>
      <rect x="368" y="15" width="14" height="9" fill="none" stroke="#fff" stroke-width="2"/>
      <circle cx="404" cy="19" r="5" fill="none" stroke="#fff" stroke-width="2.5"/>
      <rect x="424" y="14" width="16" height="10" fill="none" stroke="#fff" stroke-width="2"/>
      <path d="M452 13v4M452 13h4M468 13h-4M468 13v4M452 25v-4M452 25h4M468 25h-4M468 25v-4" stroke="#fff" stroke-width="2"/>
    </svg>
  </div>
</div>

<!-- offerings -->
<div class="abs band-edge" style="left:0"></div>
<div class="abs band-edge" style="left:1170px"></div>
<h2 class="abs sec-title" style="top:1228px">OUR <span>OFFERINGS</span></h2>
<div class="abs title-rule" style="top:1272px"></div>
<p class="abs sec-text" style="left:0;top:1296px;width:1200px"><span style="color:#f5b400">K4 Haulage</span> and Plant Hire (Pty) Ltd has expertise in the following key fields and has successfully executed projects in most of them.</p>

<div class="abs offer-card" style="left:162px">
  <svg width="50" height="50" viewBox="0 0 50 50" fill="none" stroke="#666" stroke-width="2"><rect x="4" y="14" width="26" height="20"/><path d="M30 20h8l6 8v6H30"/><circle cx="12" cy="38" r="4"/><circle cx="36" cy="38" r="4"/></svg>
  <p>Logistics And<br>Plant Hire</p>
</div>
<div class="abs offer-card active" style="left:385px">
  <svg width="50" height="50" viewBox="0 0 50 50" fill="none" stroke="#f5b400" stroke-width="2.5"><circle cx="24" cy="8" r="4"/><path d="M24 14l-4 12 6 6v12M20 26l-8 6M24 18l10 6"/><path d="M34 44l6-14 6 14z"/></svg>
  <p>Road Construction And<br>Rehabilitation</p>
</div>
<div class="abs offer-card" style="left:613px">
  <svg width="50" height="50" viewBox="0 0 50 50" fill="none" stroke="#666" stroke-width="2"><path d="M6 44L18 10h14l12 34zM25 14v6M25 26v6M25 38v4"/><path d="M10 10l4-4h22l4 4"/></svg>
  <p>Infrastructural Services<br>Development</p>
</div>
<div class="abs offer-card" style="left:836px">
  <svg width="50" height="50" viewBox="0 0 50 50" fill="none" stroke="#666" stroke-width="2"><path d="M16 16h18l-2-8H18zM18 16v8h14v-8M20 24l-4 22M30 24l4 22M18 34h14"/></svg>
  <p>Water Treatment<br>Works</p>
</div>
<svg class="abs shelf" style="top:1580px;height:24px" width="884" height="24" viewBox="0 0 884 24"><path d="M0 12h312l15-12 15 12h542" fill="none" stroke="#e8e8e8" stroke-width="2"/></svg>

<!-- why choose us -->
<h2 class="abs sec-title" style="top:1684px">WHY <span>CHOOSE US</span></h2>
<p class="abs sec-text" style="left:180px;top:1730px;width:840px;line-height:22px">Lorem ipsum dolor sit amet, consectetuer adipiscing elit, sed diam nonummy nibh euismod tincidunt ut laoreet dolore magna aliquam erat volutpat. Ut wisi enim ad minim veniam, quis nostrud exerci tation ullamcorper suscipit lobortis nisl ut aliquip ex ea commodo consequat.</p>

<svg class="abs" style="left:0;top:1780px" width="1200" height="360" viewBox="0 1780 1200 360">
  <g stroke="#cfcfcf" stroke-width="1.5">
    <line x1="600" y1="1951" x2="455" y2="1830"/><line x1="600" y1="1951" x2="409" y2="1951"/><line x1="600" y1="1951" x2="455" y2="2068"/>
    <line x1="600" y1="1951" x2="740" y2="1830"/><line x1="600" y1="1951" x2="784" y2="1951"/><line x1="600" y1="1951" x2="747" y2="2068"/>
  </g>
  <circle cx="600" cy="1951" r="124" fill="#fff" stroke="#bbb" stroke-width="2" stroke-dasharray="2 4"/>
  <circle cx="600" cy="1951" r="106" fill="#fff" stroke="#eee" stroke-width="6"/>
  <g fill="#f5b400"><circle cx="514" cy="1873" r="5"/><circle cx="477" cy="1951" r="5"/><circle cx="512" cy="2031" r="5"/><circle cx="684" cy="1873" r="5"/><circle cx="723" cy="1951" r="5"/><circle cx="688" cy="2031" r="5"/></g>
  <g>
    <g transform="translate(455 1830)"><circle r="33" fill="#f3f3f3"/><circle r="27" fill="#f5b400"/><circle r="21" fill="#2b2b2b"/><path d="M-8 6l8-14 8 14zM0 -8v-4" fill="none" stroke="#f5b400" stroke-width="2"/></g>
    <g transform="translate(409 1951)"><circle r="33" fill="#f3f3f3"/><circle r="27" fill="#f5b400"/><circle r="21" fill="#2b2b2b"/><circle cy="-4" r="5" fill="none" stroke="#f5b400" stroke-width="2"/><path d="M-9 10c0-6 18-6 18 0" fill="none" stroke="#f5b400" stroke-width="2"/></g>
    <g transform="translate(455 2068)"><circle r="33" fill="#f3f3f3"/><circle r="27" fill="#f5b400"/><circle r="21" fill="#2b2b2b"/><circle r="9" fill="none" stroke="#f5b400" stroke-width="2"/><path d="M-4 0l3 3 5-6" fill="none" stroke="#f5b400" stroke-width="2"/></g>
    <g transform="translate(740 1830)"><circle r="33" fill="#f3f3f3"/><circle r="27" fill="#f5b400"/><circle r="21" fill="#2b2b2b"/><rect x="-8" y="-8" width="16" height="16" fill="none" stroke="#f5b400" stroke-width="2"/><path d="M-4 0h8M0 -4v8" stroke="#f5b400" stroke-width="2"/></g>
    <g transform="translate(784 1951)"><circle r="33" fill="#f3f3f3"/><circle r="27" fill="#f5b400"/><circle r="21" fill="#2b2b2b"/><rect x="-9" y="-5" width="18" height="13" fill="none" stroke="#f5b400" stroke-width="2"/><path d="M-4 -5v-4h8v4" fill="none" stroke="#f5b400" stroke-width="2"/></g>
    <g transform="translate(747 2068)"><circle r="33" fill="#f3f3f3"/><circle r="27" fill="#f5b400"/><circle r="21" fill="#2b2b2b"/><circle r="9" fill="none" stroke="#f5b400" stroke-width="2"/><path d="M0 -5v5l4 3" fill="none" stroke="#f5b400" stroke-width="2"/></g>
  </g>
</svg>
<div class="abs center" style="left:500px;top:1922px;width:200px">
  <div class="hub-name">K4</div>
  <div class="brand-sub" style="color:#f5b400">HAULAGE &amp; PLANT HIRE</div>
</div>

<div class="abs trait left" style="left:143px;top:1806px"><h4>CAPABILITY</h4><p>Affording our staff, personal growth through<br>continuing education and/or training.</p></div>
<div class="abs trait left" style="left:103px;top:1926px"><h4>INTEGRITY</h4><p>Maintaining the highest<br>standards of quality.</p></div>
<div class="abs trait left" style="left:137px;top:2044px"><h4>ACCOUNTABILITY</h4><p>Providing a service to our Clients which<br>meets their expectations</p></div>
<div class="abs trait" style="left:798px;top:1806px"><h4>ADAPTABILITY</h4><p>Preparing our activities to respond to<br>the demands of the present...</p></div>
<div class="abs trait" style="left:838px;top:1926px"><h4>RELIABILITY</h4><p>Fulfilling the needs of our Clients</p></div>
<div class="abs trait" style="left:798px;top:2044px;width:320px"><h4>ETHICS</h4><p>Providing equal opportunity to all, in line with<br>Government Policies. Exerci sing zero...</p></div>

<!-- call to action -->
<div class="abs cta" role="img" aria-label="Darkened photo of a yellow excavator with an operator on site"></div>
<h2 class="abs cta-title">NEED A HIGH QUALITY CONSTUCTOR FOR YOUR PROJECT ?</h2>
<p class="abs cta-sub">We provide nationwide delivering high quality multidisciplinary engineering and construction projects</p>
<a class="abs btn cta-btn">CONTACT US TODAY</a>

<!-- footer -->
<div class="abs footer"></div>
<div class="abs" style="left:143px;top:2516px">
  <div class="foot-h" style="margin-bottom:10px">QUICK LINKS</div>
  <ul class="links"><li>Home</li><li>About Us</li><li>Offerings</li><li>Work Gallery</li><li>Contact Us</li></ul>
</div>
<div class="abs" style="left:325px;top:2516px;width:300px">
  <div class="foot-h" style="margin-bottom:14px">CONTACT DETAILS</div>
  <div class="crow"><span class="pin"><svg width="12" height="14" viewBox="0 0 12 16"><path d="M6 0a6 6 0 0 1 6 6c0 4-6 10-6 10S0 10 0 6a6 6 0 0 1 6-6z" fill="#fcc200"/></svg></span><span>P.O Box 418, Kestrel Park, 4402<br>12 Marula Road, Ashvale, Thornbury, 4404</span></div>
  <div class="crow"><span class="pin"><svg width="12" height="14" viewBox="0 0 12 16"><path d="M6 0a6 6 0 0 1 6 6c0 4-6 10-6 10S0 10 0 6a6 6 0 0 1 6-6z" fill="#fcc200"/></svg></span><span>Unit 9, Parkside Centre<br>Loxley Bay 5510</span></div>
  <div class="crow" style="align-items:center"><span class="pin"><svg width="12" height="12" viewBox="0 0 24 24"><path d="M6 2l4 4-2 3c1 3 4 6 7 7l3-2 4 4-3 4C10 22 2 14 2 5z" fill="#fcc200"/></svg></span><span style="font-size:13px">123-456-7890</span></div>
  <div class="crow" style="align-items:center"><span class="pin"><svg width="13" height="10" viewBox="0 0 24 18"><rect x="1" y="1" width="22" height="16" fill="none" stroke="#fcc200" stroke-width="3"/><path d="M1 1l11 9 11-9" fill="none" stroke="#fcc200" stroke-width="3"/></svg></span><span style="font-size:12.5px">info@k4haulage.co.za</span></div>
</div>
<div class="abs" style="left:663px;top:2516px">
  <div class="foot-h" style="margin-bottom:12px">QUICK INQUIRY</div>
  <div class="field">Name</div>
  <div class="field">Email</div>
  <div class="field msg">Message</div>
  <div class="submit" style="margin-top:8px">SUBMIT</div>
</div>
<div class="abs" style="left:910px;top:2516px">
  <div class="foot-h" style="margin-bottom:12px">FOLLOW US</div>
  <div class="socials"><i></i><i style="background:#2a9fd6"></i><i style="background:#0f6ba8"></i><i style="background:#d8344a"></i></div>
  <div style="margin-top:36px;text-align:center;width:150px">
    <div class="foot-brand">K4</div>
    <div class="brand-sub" style="color:#6b5200">HAULAGE &amp; PLANT HIRE</div>
  </div>
</div>
<div class="abs copy">Copyright © 2019 K4 Haulage &amp; Plant Hire . All Rights Reserved. &nbsp; | &nbsp; Terms of Service.</div>

</body>
</html>
```